Postcard Design Project

Services that are meant to assist farms. Company name KW FIELD SERVICES.Doing hands on work such as painting fences, Updating farm features, lawn care, rock wall restoration, farm restoration.
Updates

Target Market(s)

farm owners

Industry/Entity Type

Handyman

Colors

Designer to choose colors to be used in the design.

Requirements
Must have
• Needs to be witty and catchy to the client
Nice to have
• We want our potential clients to know that we are here to give them a hand with those projects that get left on the back burner due to time constraints.

```html
<!DOCTYPE html>
<html lang="en">
<head>
<meta charset="utf-8">
<title>KW Field Services Postcard</title>
<link href="https://fonts.googleapis.com/css2?family=Roboto:wght@300;400;700;900&family=Roboto+Condensed:wght@700&display=swap" rel="stylesheet">
<style>
  :root {
    --green: #39b54a;
    --green-light: #5cbf4a;
    --ink: #111111;
    --white: #ffffff;
    --sky-top: #f2f6fb;
    --sky-mid: #d6e8f6;
    --sky-low: #c6e2f5;
    --page-bg: #e9eef2;
  }
  html, body {
    margin: 0;
    padding: 0;
    width: 1200px;
    height: 1200px;
    overflow: hidden;
    background: var(--page-bg);
  }
  .postcard {
    position: absolute;
    left: 219px;
    top: 40px;
    width: 789px;
    height: 1160px;
    transform: scale(0.9655);
    transform-origin: 0 0;
    overflow: hidden;
    background: radial-gradient(ellipse at 50% 8%, var(--white) 0%, var(--sky-top) 25%, var(--sky-mid) 60%, var(--sky-low) 100%);
    font-family: "Roboto", Arial, sans-serif;
    color: var(--ink);
  }
  .header-band {
    position: absolute;
    left: 0;
    top: 106px;
    width: 789px;
    height: 88px;
    background: var(--green);
  }
  .band-shadow {
    position: absolute;
    top: 194px;
    height: 10px;
  }
  .band-shadow.left { left: 120px; width: 180px; background: linear-gradient(90deg, rgba(0,0,0,0), rgba(0,0,0,.75)); clip-path: polygon(0 0, 100% 0, 100% 100%); }
  .band-shadow.right { left: 510px; width: 180px; background: linear-gradient(270deg, rgba(0,0,0,0), rgba(0,0,0,.75)); clip-path: polygon(0 0, 100% 0, 0 100%); }
  .brand-disc {
    position: absolute;
    left: 289px;
    top: 36px;
    width: 230px;
    height: 230px;
    border-radius: 50%;
    background: var(--white);
    display: flex;
    align-items: center;
    justify-content: center;
  }
  .brand-mark {
    font-family: "Roboto", Arial, sans-serif;
    font-weight: 900;
    font-size: 84px;
    color: var(--green);
    letter-spacing: 2px;
  }
  .title {
    position: absolute;
    left: 0;
    width: 789px;
    text-align: center;
    margin: 0;
  }
  .title-main {
    top: 226px;
    font-family: "Roboto Condensed", Arial, sans-serif;
    font-weight: 700;
    font-size: 86px;
    line-height: 1;
    color: var(--green);
    letter-spacing: -1px;
  }
  .title-sub {
    top: 306px;
    font-weight: 400;
    font-size: 46px;
    line-height: 1;
    letter-spacing: 17px;
    padding-left: 17px;
    box-sizing: border-box;
  }
  .intro {
    position: absolute;
    left: 65px;
    top: 376px;
    width: 657px;
    margin: 0;
    font-size: 21.5px;
    line-height: 28px;
    text-align: justify;
  }
  .service-list {
    position: absolute;
    left: 62px;
    top: 510px;
    margin: 0;
    padding: 0;
    list-style: none;
  }
  .service-list li {
    position: relative;
    height: 57px;
    line-height: 38px;
    padding-left: 40px;
    font-weight: 700;
    font-size: 28px;
    text-transform: uppercase;
    letter-spacing: -0.3px;
  }
  .service-list li::before {
    content: "";
    position: absolute;
    left: 0;
    top: 7px;
    width: 25px;
    height: 25px;
    border-radius: 50%;
    background: var(--green-light);
  }
  .scene {
    position: absolute;
    left: 0;
    top: 720px;
    width: 789px;
    height: 280px;
    background: linear-gradient(180deg, rgba(57,181,74,0) 0%, rgba(57,181,74,.35) 45%, rgba(57,181,74,.9) 85%, var(--green) 100%);
  }
  .contact-band {
    position: absolute;
    left: 0;
    top: 994px;
    width: 789px;
    height: 166px;
    background: linear-gradient(180deg, var(--green) 0%, var(--green-light) 100%);
  }
  .rule {
    position: absolute;
    top: 1017px;
    height: 10px;
    border-top: 2px solid var(--white);
    border-bottom: 2px solid var(--white);
    box-sizing: border-box;
  }
  .rule::after {
    content: "";
    position: absolute;
    left: 0;
    right: 0;
    top: 2px;
    border-top: 2px solid var(--white);
  }
  .rule.left { left: 0; width: 219px; }
  .rule.right { left: 579px; width: 210px; }
  .contact-heading {
    position: absolute;
    left: 0;
    top: 1001px;
    width: 789px;
    margin: 0;
    text-align: center;
    font-weight: 300;
    font-size: 37px;
    line-height: 46px;
    color: var(--white);
  }
  .contact-line {
    position: absolute;
    left: 0;
    top: 1050px;
    width: 789px;
    display: flex;
    justify-content: center;
    align-items: center;
    gap: 28px;
    font-weight: 700;
    font-size: 40px;
    line-height: 52px;
    color: var(--white);
  }
  .contact-item {
    display: flex;
    align-items: center;
    gap: 6px;
  }
  .contact-item svg { width: 34px; height: 40px; }
  .contact-at { color: var(--ink); font-weight: 700; }
</style>
</head>
<body>
  <main class="postcard">
    <div class="header-band"></div>
    <div class="band-shadow left"></div>
    <div class="band-shadow right"></div>
    <div class="brand-disc"><span class="brand-mark">KW</span></div>

    <h1 class="title title-main">KW FIELD</h1>
    <p class="title title-sub">SERVICES</p>

    <p class="intro">Our company is the leading company known for Contract Farming Service to the clients. We are offering these services by our experienced professionals who have complete knowledge of this field and understand the exact demands of clients.</p>

    <ul class="service-list">
      <li>Painting Fences</li>
      <li>Updating Farm Features</li>
      <li>Lawn Care</li>
      <li>Farm Restoration</li>
      <li>Rock Wall Restoration</li>
    </ul>

    <div class="scene" role="img" aria-label="Green grass silhouette with a lawn mower silhouette on the right"></div>

    <section class="contact-band"></section>
    <div class="rule left"></div>
    <div class="rule right"></div>
    <h2 class="contact-heading">CONTACT US NOW</h2>
    <div class="contact-line">
      <span class="contact-item">
        <svg viewBox="0 0 24 28" aria-hidden="true"><path fill="#111" d="M6 2 L10 2 L11 9 L8 11 C9 15 11 18 14 20 L16 17 L22 19 L22 24 C22 26 20 27 18 26 C10 23 4 15 3 6 C3 4 4 2 6 2 Z"/></svg>
        555 014 278
      </span>
      <span class="contact-item"><span class="contact-at">@</span> hello@kwfield.com</span>
    </div>
  </main>
</body>
</html>
```